Cozy Sprouts Business Cards

I need a business card for my new Company called Cozy Sprouts. We create handmade baby moccasins, headbands, t-shirts and more. I want some that will appeal to parents, and to go with the colors of my logo that I have attached. feel free to be creative. I would like my logo placed somewhere on the card.

Industry/Entity Type

Retail

Contact Information for Business Card

Cozy Sprouts
24816 Maplecrest D #5172
Irvine Ca 92738
Rosalind Vantrey Ceo
Info@Cozy-Sprouts.com
www.Cozy-Sprouts.com
Phone 9495817320

Requirements
Nice to have
• Logo included

```html
<!DOCTYPE html>
<html lang="en">
<head>
<meta charset="utf-8">
<title>Cozy Sprouts Business Cards</title>
<link href="https://fonts.googleapis.com/css2?family=Comic+Neue:wght@400;700&family=Bitter:wght@400&display=swap" rel="stylesheet">
<style>
  :root {
    --backdrop: #4a403b;
    --card-black: #0d0d0e;
    --card-white: #fbfbfa;
    --accent-orange: #e07b45;
    --text-light: #f2f2f2;
    --text-dark: #141414;
  }
  * { margin: 0; padding: 0; box-sizing: border-box; }
  html, body {
    width: 1200px; height: 768px; overflow: hidden;
    background: var(--backdrop);
  }
  .canvas { position: relative; width: 1200px; height: 768px; }
  .card {
    position: absolute; width: 540px; height: 310px; top: 229px;
    box-shadow: 0 10px 24px rgba(0,0,0,0.45);
    overflow: hidden;
  }
  .card-front { left: 40px; background: var(--card-black); }
  .card-back { left: 620px; background: var(--card-white); }

  .wordmark {
    position: absolute; display: flex; align-items: center; gap: 12px;
    font-family: "Comic Neue", "Comic Sans MS", cursive;
    font-weight: 400; font-size: 44px; white-space: nowrap;
  }
  .wordmark-square { width: 22px; height: 22px; background: var(--accent-orange); flex: none; }
  .card-front .wordmark { left: 50%; top: 50%; transform: translate(-50%, -50%); color: var(--text-light); }
  .card-back .wordmark { left: 30px; top: 136px; font-size: 36px; color: var(--text-dark); }

  .back-shape { position: absolute; inset: 0; }

  .contact {
    position: absolute; left: 340px; top: 62px; color: var(--text-light);
  }
  .contact-name {
    font-family: "Comic Neue", "Comic Sans MS", cursive; font-weight: 700;
    font-size: 21px; color: var(--accent-orange); letter-spacing: 0.3px;
  }
  .contact-title {
    font-family: "Bitter", Georgia, serif; font-size: 10px; margin-top: 2px;
  }
  .contact-address {
    font-family: "Bitter", Georgia, serif; font-size: 12.5px; line-height: 1.45;
    margin-top: 34px;
  }
  .contact-list { list-style: none; margin-top: 14px; font-family: "Bitter", Georgia, serif; font-size: 12.5px; }
  .contact-list li { display: flex; align-items: center; gap: 8px; line-height: 1.55; }
  .contact-list svg { width: 11px; height: 11px; flex: none; }
</style>
</head>
<body>
<div class="canvas">

  <section class="card card-front">
    <div class="wordmark"><span class="wordmark-square"></span>Cozy Sprouts</div>
  </section>

  <section class="card card-back">
    <svg class="back-shape" viewBox="0 0 540 310" aria-hidden="true">
      <path d="M318 0 Q352 160 230 310 L540 310 L540 0 Z" fill="var(--card-black)"/>
      <path d="M304 0 Q352 150 222 310" fill="none" stroke="var(--accent-orange)" stroke-width="4"/>
    </svg>

    <div class="wordmark"><span class="wordmark-square"></span>Cozy Sprouts</div>

    <div class="contact">
      <div class="contact-name">Rosalind Vantrey</div>
      <div class="contact-title">CEO</div>
      <div class="contact-address">24816 Maplecrest D #5172<br>Irvine Ca 92738</div>
      <ul class="contact-list">
        <li>
          <svg viewBox="0 0 12 12"><path d="M2 1h2.5l1 3-1.5 1a7 7 0 0 0 3 3l1-1.5 3 1V11h-1A9 9 0 0 1 1 2V1z" fill="var(--accent-orange)"/></svg>
          9495817320
        </li>
        <li>
          <svg viewBox="0 0 12 12"><rect x="0.5" y="2" width="11" height="8" fill="var(--accent-orange)"/><path d="M0.5 2 6 7l5.5-5" fill="none" stroke="var(--card-black)" stroke-width="1"/></svg>
          Info@Cozy-Sprouts.com
        </li>
        <li>
          <svg viewBox="0 0 12 12"><circle cx="6" cy="6" r="5.5" fill="var(--accent-orange)"/><path d="M0.5 6h11M6 0.5c-3 3-3 8 0 11M6 0.5c3 3 3 8 0 11" fill="none" stroke="var(--card-black)" stroke-width="0.8"/></svg>
          www.Cozy-Sprouts.com
        </li>
      </ul>
    </div>
  </section>

</div>
</body>
</html>
```